KTR Global corporate slide deck

We are looking for a custom powerpoint template to use both internally and externally with clients and during trainings/presentations. Our customers/clients often include a lot of government agencies, and we specialize in forensics, biometrics, and identity intelligence.
Requirements:
• Title slide
• Section slide
• Title and content slide
• Every slide branded
• Every slide (other than title) includes slide number (x of y), title, and date
• Modern-looking but conservative
• Visually appealing
• Source Sans Pro font
• Call out boxes

The circle in our logo does not signify or mean anything in any way, but we also don't mind it being used as a design element. We also like pulling the blue to red gradient.
Ideally we do not want to use any images of people, but iconography is likely okay.

```html
<!DOCTYPE html>
<html lang="en">
<head>
<meta charset="UTF-8">
<title>KTR Global – Foster Growth</title>
<link href="https://fonts.googleapis.com/css2?family=Bebas+Neue&family=Source+Sans+3:wght@400;600;700&display=swap" rel="stylesheet">
<style>
  :root {
    --brand-purple: #43175e;
    --brand-purple-soft: #5a2a78;
    --accent-pink: #e0196e;
    --white: #ffffff;
    --footer-grey: #8a8a8a;
    --page-bg: #ffffff;
  }
  * { margin: 0; padding: 0; box-sizing: border-box; }
  html, body {
    width: 1200px;
    height: 675px;
    overflow: hidden;
    background: var(--page-bg);
  }
  .slide {
    position: relative;
    width: 1200px;
    height: 675px;
    background: var(--page-bg);
    font-family: "Source Sans 3", "Source Sans Pro", sans-serif;
  }
  .brand-mark {
    position: absolute;
    top: 60px;
    right: 66px;
    display: flex;
    align-items: center;
    gap: 8px;
    color: var(--brand-purple);
    font-weight: 700;
    font-size: 17px;
  }
  .brand-mark__dot {
    width: 14px;
    height: 14px;
    border-radius: 50%;
    background: var(--accent-pink);
  }
  .feature-panel {
    position: absolute;
    left: 54px;
    top: 143px;
    width: 1092px;
    height: 445px;
    background: var(--brand-purple);
  }
  .feature-panel__title {
    position: absolute;
    left: 71px;
    top: 78px;
    font-family: "Bebas Neue", "Oswald", sans-serif;
    font-weight: 400;
    font-size: 66px;
    line-height: 79px;
    color: var(--white);
    letter-spacing: 0.5px;
  }
  .feature-panel__quote {
    position: absolute;
    left: 71px;
    top: 236px;
    width: 28px;
    height: 28px;
  }
  .feature-panel__body {
    position: absolute;
    left: 111px;
    top: 252px;
    width: 580px;
    font-size: 15.5px;
    font-weight: 600;
    line-height: 21.5px;
    color: var(--white);
  }
  .feature-panel__art {
    position: absolute;
    left: 787px;
    top: 144px;
    width: 235px;
    height: 203px;
    border-radius: 12px;
    background: radial-gradient(circle at 45% 45%, var(--accent-pink) 0%, var(--brand-purple-soft) 55%, var(--brand-purple) 100%);
    opacity: 0.55;
  }
  .slide-footer {
    position: absolute;
    left: 54px;
    right: 54px;
    top: 643px;
    display: flex;
    justify-content: space-between;
    font-size: 9px;
    color: var(--footer-grey);
    letter-spacing: 0.2px;
  }
</style>
</head>
<body>
  <div class="slide">
    <div class="brand-mark">
      <span class="brand-mark__dot"></span>
      <span class="brand-mark__name">KTR Global</span>
    </div>

    <section class="feature-panel">
      <h1 class="feature-panel__title">Foster growth with clear<br>investment principles</h1>
      <svg class="feature-panel__quote" viewBox="0 0 28 28" aria-hidden="true">
        <path d="M2 2h9v9c0 6-3 11-6 15l-3-1c2-3 3-6 3-9H2z" fill="#ffffff"/>
        <path d="M15 2h9v9c0 6-3 11-6 15l-3-1c2-3 3-6 3-9h-3z" fill="#ffffff"/>
      </svg>
      <p class="feature-panel__body">Lorem ipsum dolor sit amet, consectetuer adipiscing elit. Aenean commodo ligula eget dolor. Aenean massa. Cum sociis natoque penatibus et magnis dis parturient montes, nascetur ridiculus mus. Donec quam felis, ultricies nec, pellentesque eu, pretium quis, sem. Nulla consequat massa quis enim. Donec pede justo, fringilla vel, aliquet nec, vulputate eget, arcu.</p>
      <div class="feature-panel__art" role="img" aria-label="Icon cluster illustration: magnifying glass with checklist, target, award ribbon and hand holding a growing coin plant"></div>
    </section>

    <footer class="slide-footer">
      <span class="slide-footer__date">26.06.24</span>
      <span class="slide-footer__title">DATE | PRESENTATION TITLE</span>
      <span class="slide-footer__number">7</span>
    </footer>
  </div>
</body>
</html>
```